new KVR one page flyer

We need a 1 page A4 size flyer (need it asap please) that describes on 1 page with art work and using photos the services we provide. I have included some examples of old previous flyers from our other (seperate divisions of the business) I have named a photo called (photo for top of design) however you do your design this photo needs to be the star of the page by either having it at the top or bottom of the page please and we usually like this photo to be in greyscale colour.
we do like greyscale designs but are open to see what you come up with as a whole page of grey white and black might not suit.

Needs to list the following

Services include:
Over size loads / Hot Shot Loads
Heavy Vehicle Recovery services
Potable Water Deliveries
Road Building / Maintenance
Earthworks
Sand & Metal Supply & Cartage
Road Train Tippers
Road Train Tankers
Road Train Flat Tops
Drop Deck Trailers
Mine site accredited equipment & Operators.

We offer a large rage of services not listed so call us today for a personalised quote to suit your needs.

To go on the bottom of the page our contact details are

KVR Pty Ltd
Depot: Lot 514, Banksia Flats Track Coober Pedy
Mobile: 047 216 9381
email: darren@kestrelvaleroadworks.com.au

Target Market(s)

new clients

Colors

Designer to choose colors to be used in the design.

Requirements
Must have
• our services listed
Nice to have
• stand out designs

```html
<!DOCTYPE html>
<html lang="en">
<head>
<meta charset="utf-8">
<title>KVR Services Flyer</title>
<link href="https://fonts.googleapis.com/css2?family=Archivo:wght@400;700;800&display=swap" rel="stylesheet">
<style>
  :root {
    --ink: #1c1c1c;
    --paper: #ffffff;
    --dark-panel: #2a2a2a;
    --dark-panel-2: #0f0f0f;
    --muted: #4a4a4a;
    --photo-sky: #f2f2f2;
    --photo-ground: #9a9a9a;
  }
  html, body {
    margin: 0;
    padding: 0;
    overflow: hidden;
    background: var(--paper);
  }
  .flyer {
    position: relative;
    width: 857px;
    height: 1200px;
    overflow: hidden;
    background: var(--paper);
    font-family: "Archivo", Arial, sans-serif;
    color: var(--ink);
  }
  .brand-panel {
    position: absolute;
    left: 29px;
    top: 0;
    width: 186px;
    height: 343px;
    background: linear-gradient(160deg, var(--dark-panel) 0%, var(--dark-panel-2) 100%);
  }
  .brand-name {
    position: absolute;
    left: 0;
    width: 100%;
    top: 248px;
    text-align: center;
    font-weight: 800;
    font-size: 46px;
    letter-spacing: 4px;
    color: var(--paper);
  }
  .services-heading {
    position: absolute;
    left: 329px;
    top: 206px;
    width: 520px;
    height: 45px;
    box-sizing: border-box;
    border: 2px solid var(--ink);
    text-align: right;
    padding-right: 24px;
    line-height: 41px;
    font-size: 21px;
    font-weight: 700;
    letter-spacing: 5px;
  }
  .service-list {
    position: absolute;
    right: 28px;
    top: 272px;
    margin: 0;
    padding: 0;
    list-style: none;
    text-align: right;
  }
  .service-list li {
    font-size: 28px;
    font-weight: 800;
    line-height: 31px;
    letter-spacing: -0.2px;
  }
  .intro {
    position: absolute;
    right: 28px;
    top: 612px;
    margin: 0;
    width: 520px;
    text-align: right;
    font-size: 14.5px;
    line-height: 22px;
    color: var(--muted);
  }
  .contact {
    position: absolute;
    right: 28px;
    top: 710px;
    margin: 0;
    text-align: right;
    font-style: normal;
    font-size: 16px;
    font-weight: 700;
    line-height: 22px;
  }
  .hero-photo {
    position: absolute;
    left: 0;
    top: 857px;
    width: 857px;
    height: 343px;
    background: linear-gradient(180deg, var(--paper) 0%, var(--photo-sky) 35%, #6f6f6f 62%, var(--photo-ground) 100%);
  }
</style>
</head>
<body>
  <main class="flyer">
    <div class="brand-panel">
      <div class="brand-name">KVR</div>
    </div>

    <h2 class="services-heading">SERVICES INCLUDE</h2>

    <ul class="service-list">
      <li>Over size loads / Hot Shot Loads</li>
      <li>Heavy Vehicle Recovery services</li>
      <li>Potable Water Deliveries</li>
      <li>Road Building / Maintenance</li>
      <li>Earthworks</li>
      <li>Sand &amp; Metal Supply &amp; Cartage</li>
      <li>Road Train Tippers</li>
      <li>Road Train Tankers</li>
      <li>Road Train Flat Tops</li>
      <li>Drop Deck Trailers</li>
    </ul>

    <p class="intro">
      Mine site accredited equipment &amp; Operators.<br>
      We offer a large rage of services not listed so call us<br>
      today for a personalised quote to suit your needs.
    </p>

    <address class="contact">
      KVR Pty Ltd<br>
      Depot: Lot 514, Banksia Flats Track Coober Pedy<br>
      Mobile: 047 216 9381<br>
      Email: darren@kestrelvaleroadworks.com.au
    </address>

    <div class="hero-photo" role="img" aria-label="Greyscale photo of a road train truck with side tipper trailers driving on an outback dirt road"></div>
  </main>
</body>
</html>
```